Jewelry store needs fully functional Ecommerce website

Web Design Brief for our E-commerce Jewelry retail store.
Description

We need a fully coded Vendora website. The Vendora site will need to be fully functional with an Ecommerce integration (fully integrated with Coinlet and All other gateways) and will need to be SEO optimized.
We sell jewelry items like: rings, earrings, necklaces etc. The website should have an elegant, modern, professional, fun, look.

***We would like the website to look and function similarly to this website:
https://velvetrune.com

Color Preference
Colors to be used are white background with black font and light pink/ purple/ gold tints. We have attached our logo as reference.

Functionalities
The store will function like a typical Ecommerce jewelry store, using the products/categories as the starting page. Going into individual product pages by selecting images and leading to a detailed “buy now” page for the selected product.

Target Market
Jewelry lovers.

Should Not Have:
- - Dull and common design
- - Messy/unstructured navigation

Coded - Design and coding required
Target Audience are women from 16-50 years old.
We will need to be able to add products and make modifications to the website as needed.

We need the following apps installed and Operating:
-Shelf Tally; Parcel Finder (rename “track your order”) ; Query Desk (Questions and Answers) ; Vimt Reviews; Textazo; Brundel Email Marketing ; Tavolo (Chatterloop messenger bump) ; Brisk multi- currency (translate currency to buyer) ; Pricewise Extra ; Swift Reach form App
We will need all products imported: (below is information for importing products). We will provide all links that serve entire active item product catalog in vendoras import format:
DataFeed:

If you are getting started with Vendora, a combination of the Vendora Import Format and XML feeds is ideal. The Vendora Import Format will output a file that can be uploaded into Vendora’s product database. After you import, you can use the XML feed and a third party app to keep the inventory up to date in real time, take down items that go out of stock etc., all without regular human intervention. There a several Vendora apps that can do this type of feed integration. We have had a good experience with Shelf Tally, which is an app that can be configured to accept our XML feed and update products on a set schedule. You can even set your own margins based on our wholesale price with this app.

Vendora Formatted HTML TableTo make it easier to get started on Vendora, we included a format that outputs the required fields for a product import in Vendora. In order to use the embedded Excel file, first open the file (Auto-Vendora-Datasheet-Format.xslx), Refresh it (under Data tab), and then Save As with a new file name in a CSV (UTF-8) file. That file can then be split into smaller CSV files (if there is a limit on the number of products per file) for import into Vendora.

Target Market(s)

Jewelry Lovers

Industry/Entity Type

Jewelry Store

Coding

Number of Pages Required

5+ page

Colors
eda3c7
d3a5cc
ffffff

Requirements
Must have
• Color Preference
Colors to be used are white background with black font and light pink/ purple/ gold tints.

https://velvetrune.com
Should not have
• Should Not Have:

```html
<!DOCTYPE html>
<html lang="en">
<head>
<meta charset="utf-8">
<title>Everlume — Find Your Favorite Jewelry</title>
<link href="https://fonts.googleapis.com/css2?family=Cormorant+Garamond:wght@400;500&family=Mulish:wght@400;500;600;700&display=swap" rel="stylesheet">
<style>
:root{
  --plum:#4a2c4e;
  --plum-deep:#3f2744;
  --plum-btn:#4d2a4f;
  --ink:#2b2b2b;
  --muted:#555;
  --pink:#eda3c7;
  --lilac:#d3a5cc;
  --white:#ffffff;
  --gold:#c9a36a;
  --serif:'Cormorant Garamond', Georgia, serif;
  --sans:'Mulish', Arial, sans-serif;
}
*{box-sizing:border-box;margin:0;padding:0}
html,body{width:1200px;height:2560px;overflow:hidden}
body{position:relative;background:var(--white);font-family:var(--sans);color:var(--ink)}
.abs{position:absolute}

/* header */
.site-header{left:0;top:0;width:1200px;height:107px;background:var(--white)}
.brand{left:44px;top:18px;text-align:center;width:230px}
.brand-name{font-family:var(--serif);font-size:42px;color:var(--ink);line-height:1}
.brand-sub{font-family:var(--sans);font-size:11px;letter-spacing:2.5px;color:var(--gold);margin-top:8px}
.main-nav{left:365px;top:58px;display:flex;gap:0}
.main-nav span{font-size:16px;font-weight:600;color:var(--plum);margin-right:28px;letter-spacing:.2px}
.main-nav span.has-menu::after{content:"⌄";font-size:12px;margin-left:3px;position:relative;top:-3px}
.header-icons{left:1025px;top:40px;display:flex;gap:30px;align-items:center}

/* hero */
.hero{left:0;top:107px;width:1200px;height:614px;
  background:linear-gradient(100deg,#d9c3ad 0%,#c9a17e 30%,#b48857 60%,#9a6b35 100%)}
.hero-title{left:505px;top:300px;font-family:var(--serif);font-size:92px;color:var(--white);line-height:1;letter-spacing:1px}
.hero-sub{left:503px;top:388px;font-family:var(--serif);font-size:40px;color:var(--white);letter-spacing:.5px}
.hero-cta{left:508px;top:460px;width:330px;height:64px;background:var(--pink);border-radius:6px;color:var(--white);
  font-size:46px;text-align:center;line-height:64px;font-family:var(--sans);font-weight:400}

/* category tiles */
.tile{width:400px}
.tile-art{position:absolute;inset:0}
.tile-copy{position:absolute}
.tile-copy .rule{width:48px;height:1px;background:currentColor;opacity:.7;margin-bottom:8px}
.tile-copy h2{font-family:var(--serif);font-weight:400;font-size:31px;line-height:35px}
.btn{display:inline-block;font-size:11px;letter-spacing:1.5px;padding:0 18px;height:30px;line-height:30px;margin-top:20px;font-family:var(--sans);font-weight:600}
.btn-dark{background:var(--plum-btn);color:var(--white)}
.btn-light{background:var(--white);color:var(--plum)}
.dark-text{color:var(--plum)}
.light-text{color:var(--white)}

/* promo */
.promo{left:0;top:1285px;width:1200px;height:300px;background:radial-gradient(circle at 30% 40%,#fbe7b9,#f6d88f 70%,#f1cf82)}
.promo-art{left:110px;top:70px;width:480px;height:160px;border-radius:40px;background:linear-gradient(90deg,#d9dde3,#b7bec8,#e6e9ee)}
.promo-copy{left:730px;top:70px;color:var(--plum)}
.promo-copy .rule{width:48px;height:1px;background:var(--plum);margin-bottom:10px}
.promo-copy h2{font-family:var(--serif);font-weight:400;font-size:30px}
.promo-copy p{font-size:12px;line-height:20px;color:var(--muted);margin-top:10px}

/* partners */
.partners{left:0;top:1585px;width:1200px;height:150px;display:flex;align-items:center;justify-content:space-around;padding:0 30px}
.partner{font-family:var(--sans);font-size:20px;color:#333;letter-spacing:2px;display:flex;align-items:center;gap:8px}
.partner .dot{width:10px;height:10px;border-radius:50%;background:#333}

/* blog */
.blog-intro{left:0;top:1735px;width:300px;height:300px;background:#d4c6d8;text-align:center;color:var(--plum)}
.blog-intro h2{font-family:var(--serif);font-size:32px;font-weight:500;margin-top:80px}
.blog-intro p{font-size:11px;line-height:17px;color:var(--muted);margin:12px 30px 0}
.blog-intro .link{display:inline-block;margin-top:22px;font-size:10px;letter-spacing:1.5px;color:#8a7f90;border-bottom:1px solid #8a7f90;padding-bottom:4px}
.post{top:1735px;width:300px;height:300px}
.post-copy{position:absolute;left:32px;top:125px;width:245px;color:var(--white)}
.post-copy .rule{width:48px;height:1px;background:var(--white);opacity:.6;margin-bottom:8px}
.post-copy h3{font-family:var(--serif);font-weight:400;font-size:18px;line-height:22px;height:70px}
.post-copy .read{display:inline-block;border:1px solid rgba(255,255,255,.6);font-size:10px;letter-spacing:1.5px;padding:0 22px;height:28px;line-height:28px;margin-top:20px}

/* newsletter */
.newsletter{left:0;top:2035px;width:1200px;height:227px;background:linear-gradient(180deg,#f1e4ef,#fbe8ea);text-align:center;color:var(--plum)}
.newsletter h2{font-family:var(--serif);font-size:32px;font-weight:500;margin-top:24px}
.newsletter p{font-size:11px;line-height:17px;color:var(--muted);margin-top:14px}
.news-form{display:flex;justify-content:center;gap:6px;margin-top:20px}
.news-input{width:226px;height:30px;border:1px solid #c7a6b8;background:rgba(255,255,255,.4);font-size:9px;line-height:30px;color:#777}
.news-btn{width:112px;height:30px;background:var(--white);font-size:10px;letter-spacing:1.5px;line-height:30px;color:var(--plum)}

/* footer */
.site-footer{left:0;top:2262px;width:1200px;height:298px;background:var(--plum-deep);color:#e6dbe8}
.fcol{position:absolute;top:40px}
.fcol h4{font-family:var(--serif);font-size:12px;letter-spacing:1.5px;font-weight:600;color:var(--white);border-top:1px solid rgba(255,255,255,.5);display:inline-block;padding-top:4px;width:50px;white-space:nowrap}
.fcol ul{list-style:none;font-size:9.5px;line-height:19px;margin-top:20px}
.score{font-size:28px;font-weight:600;color:var(--white);display:flex;align-items:center;gap:10px;margin-top:20px}
.score small{font-size:9px;line-height:11px;font-weight:500}
.stars{color:#f2c94c;font-size:18px;letter-spacing:2px;margin-top:2px}
.fine{font-size:7.5px;margin-top:6px}
.btn-reviews{display:inline-block;background:#8a7396;color:var(--white);font-size:9px;letter-spacing:1px;padding:0 15px;height:22px;line-height:22px;margin-top:14px}
.socials{display:flex;gap:12px;margin-top:16px}
.socials span{width:28px;height:28px;border-radius:50%;background:#7c6a83}
.legal{left:97px;top:254px;display:flex;align-items:center;font-size:15px;color:#e8dfea}
.legal .sep{width:1px;height:28px;background:rgba(255,255,255,.4);margin:0 12px}
.pay{left:940px;top:2532px;display:flex;gap:12px}
.pay span{width:32px;height:18px;background:#d9d2db;border-radius:2px;font-size:6px;color:var(--plum);text-align:center;line-height:18px;font-weight:700}
</style>
</head>
<body>

<header class="site-header abs">
  <div class="brand abs">
    <div class="brand-name">Everlume</div>
    <div class="brand-sub">BY MIRA AND JOLENE</div>
  </div>
  <nav class="main-nav abs">
    <span class="has-menu">RINGS</span><span>DIAMONDS</span><span class="has-menu">JEWELRY</span><span class="has-menu">WATCHES</span><span class="has-menu">BLOG</span><span class="has-menu">ABOUT</span>
  </nav>
  <div class="header-icons abs">
    <svg width="30" height="30" viewBox="0 0 30 30" aria-label="Search"><circle cx="12" cy="12" r="9" fill="none" stroke="#222" stroke-width="3"/><line x1="19" y1="19" x2="27" y2="27" stroke="#222" stroke-width="3.5" stroke-linecap="round"/></svg>
    <svg width="36" height="38" viewBox="0 0 36 38" aria-label="Account"><circle cx="18" cy="11" r="8.5" fill="none" stroke="#222" stroke-width="2"/><path d="M3 36c0-9 6-15 15-15s15 6 15 15z" fill="none" stroke="#222" stroke-width="2"/></svg>
    <svg width="38" height="38" viewBox="0 0 38 38" aria-label="Cart, 3 items"><path d="M4 12h26l-2 24H6z" fill="none" stroke="#222" stroke-width="2"/><path d="M11 14v-4a6 6 0 0 1 12 0v4" fill="none" stroke="#222" stroke-width="2"/><circle cx="32" cy="6" r="5" fill="#222"/><text x="32" y="9" font-size="8" fill="#fff" text-anchor="middle" font-family="Mulish,sans-serif">3</text></svg>
  </div>
</header>

<section class="hero abs" role="img" aria-label="Portrait photo of a woman wearing gold earrings and rings">
</section>
<h1 class="hero-title abs">EVERLUME</h1>
<div class="hero-sub abs">FIND YOUR FAVORITE JEWELRY</div>
<div class="hero-cta abs">SHOP NOW</div>

<!-- row 1 -->
<section class="tile abs" style="left:0;top:721px;height:265px">
  <div class="tile-art" role="img" aria-label="Photo of a solitaire engagement ring setting" style="background:linear-gradient(110deg,#f3f1f7,#e4dced 60%,#cbb9da)"></div>
  <div class="tile-copy dark-text" style="left:212px;top:84px"><div class="rule"></div><h2>Engagement<br>Rings</h2><span class="btn btn-dark">SHOP NOW</span></div>
</section>
<section class="tile abs" style="left:400px;top:721px;height:265px">
  <div class="tile-art" role="img" aria-label="Photo of stacked diamond wedding bands" style="background:linear-gradient(160deg,#6f7a96,#46506e 50%,#3a2f52)"></div>
  <div class="tile-copy light-text" style="left:56px;top:94px"><h2>Wedding<br>Rings</h2><span class="btn btn-light">SHOP NOW</span></div>
</section>
<section class="tile abs" style="left:800px;top:721px;height:265px">
  <div class="tile-art" role="img" aria-label="Photo of loose pear-cut diamonds on sand" style="background:linear-gradient(100deg,#b9b8b6,#e7dfd6 50%,#efe7df)"></div>
  <div class="tile-copy dark-text" style="left:225px;top:84px"><div class="rule"></div><h2>Certified<br>Diamonds</h2><span class="btn btn-dark">SHOP NOW</span></div>
</section>

<!-- row 2 -->
<section class="tile abs" style="left:0;top:986px;height:300px">
  <div class="tile-art" role="img" aria-label="Photo of an infinity pendant necklace beside a gift box" style="background:linear-gradient(160deg,#5a3d5a,#4a2c47 60%,#3c2439)"></div>
  <div class="tile-copy light-text" style="left:55px;top:118px"><div class="rule"></div><h2>Jewelry<br>&amp; Gifts</h2><span class="btn btn-light">SHOP NOW</span></div>
</section>
<section class="tile abs" style="left:400px;top:986px;height:300px">
  <div class="tile-art" role="img" aria-label="Illustration of a ring being designed on a tablet" style="background:linear-gradient(120deg,#f0eff0,#e3e1e3 60%,#c9c6cb)"></div>
  <div class="tile-copy dark-text" style="left:225px;top:118px"><div class="rule"></div><h2>Custom<br>Design</h2><span class="btn btn-dark">START NOW</span></div>
</section>
<section class="tile abs" style="left:800px;top:986px;height:300px">
  <div class="tile-art" role="img" aria-label="Photo of a silver luxury wristwatch" style="background:linear-gradient(160deg,#3d2e48,#2f2440 60%,#3a2c44)"></div>
  <div class="tile-copy light-text" style="left:55px;top:118px"><div class="rule"></div><h2>Luxury<br>Watches</h2><span class="btn btn-light">SHOP NOW</span></div>
</section>

<!-- promo -->
<section class="promo abs">
  <div class="promo-art abs" role="img" aria-label="Photo of four designer engagement rings"></div>
  <div class="promo-copy abs">
    <div class="rule"></div>
    <h2>Experience Corvessa</h2>
    <p>Ultimate symbol of commitment.<br>Express your style. Personalize your dream ring.</p>
    <span class="btn btn-dark">SHOP NOW</span>
  </div>
</section>

<!-- partners -->
<section class="partners abs" aria-label="Brands we carry">
  <div class="partner">HALVERN</div>
  <div class="partner"><span class="dot"></span>CORVESSA</div>
  <div class="partner">Lunaria</div>
  <div class="partner">OSTRAND</div>
  <div class="partner">BELMIRA</div>
  <div class="partner" style="font-family:var(--serif);font-size:26px;letter-spacing:0">Everlume</div>
</section>

<!-- blog -->
<section class="blog-intro abs">
  <h2>Blog</h2>
  <p>Our thoughts, news, tips and suggestions on various precious themes</p>
  <span class="link">VIEW ALL ARTICLES ›</span>
</section>
<article class="post abs" style="left:300px">
  <div class="tile-art" role="img" aria-label="Photo of a woman wearing hoop earrings" style="background:linear-gradient(180deg,#6a4a5a,#4d3046 60%,#3e2740)"></div>
  <div class="post-copy"><div class="rule"></div><h3>Pearls of Wisdom - Great tips and tricks to keeping your jewelry safe and looking great!</h3><span class="read">READ MORE</span></div>
</article>
<article class="post abs" style="left:600px">
  <div class="tile-art" role="img" aria-label="Photo of a brilliant-cut diamond" style="background:radial-gradient(circle at 50% 25%,#8d7a8c,#5a4258 50%,#46304a)"></div>
  <div class="post-copy"><div class="rule"></div><h3>Lab Created Diamonds VS Real Diamonds – Facts You Need to Know</h3><span class="read">READ MORE</span></div>
</article>
<article class="post abs" style="left:900px">
  <div class="tile-art" role="img" aria-label="Photo of the store building exterior" style="background:linear-gradient(180deg,#8a6f74,#5c4356 55%,#4a3150)"></div>
  <div class="post-copy"><div class="rule"></div><h3>Grand Re-Opening Sale April 9th - May 9th - 20-50% off</h3><span class="read">READ MORE</span></div>
</article>

<!-- newsletter -->
<section class="newsletter abs">
  <h2>Newsletter</h2>
  <p>We'll deliver gorgeous jewelry right to your inbox<br>Subscribe to our product updates:</p>
  <div class="news-form"><div class="news-input">Email Address</div><div class="news-btn">SUBSCRIBE</div></div>
</section>

<!-- footer -->
<footer class="site-footer abs">
  <div class="fcol" style="left:100px">
    <h4>CONTACT US</h4>
    <ul><li>0000, road,</li><li>House.Country</li><li>000-000-0000</li><li>www.everlume.com</li></ul>
    <div class="socials" aria-label="Social links"><span></span><span></span><span></span><span></span></div>
  </div>
  <div class="fcol" style="left:368px">
    <h4>REVIEWS</h4>
    <div class="score">5.0 <small>OUT OF<br>5 STARS</small></div>
    <div class="stars">★★★★★</div>
    <div class="fine">Based on 17 first-party reviews</div>
    <span class="btn-reviews">VIEW REVIEWS</span>
  </div>
  <div class="fcol" style="left:599px">
    <h4>SHOP</h4>
    <ul><li>Engagement Rings</li><li>Ladies Wedding Rings</li><li>Mans Wedding Rings</li><li>Diamonds</li><li>Custom Jewelry</li><li>Harlow Collection</li></ul>
  </div>
  <div class="fcol" style="left:741px;top:64px">
    <ul><li>Accesories</li><li>Bracelets</li><li>Earrings</li><li>Pendants &amp; Necklaces</li><li>Watches</li></ul>
  </div>
  <div class="fcol" style="left:956px">
    <h4>COMPANY</h4>
    <ul><li>About Us</li><li>Reviews</li><li>Blog</li><li>Contact Us</li></ul>
  </div>
  <div class="legal abs">
    <span>2021 everlume is a resisterd trademark.all right reserver</span><span class="sep"></span><span>tearm and conditions</span><span class="sep"></span><span>privacy policy</span>
  </div>
</footer>
<div class="pay abs" aria-label="Accepted payments"><span>Cardo</span><span>Vexa</span><span>Dispa</span><span>Coinlet</span></div>

</body>
</html>
```